Neighbor of existing customer door hanger

We are a landscaping services company (Pest Control & Lawn Fertilization). I am looking for a piece that my sales people can leave behind at the neighbors of our current customers offering our services to them.

I'm not a graphics guy, not even close, I started making a sample that is not any good, but it might give the general idea. I have attached that design here. There is a template available from the printer for 4.25 x 11". I have included that as well

Target Market(s)

Women homeowners 35-50

Industry/Entity Type

Landscape Gardening

Font styles to use
Sans Serif

Colors

Designer to choose colors to be used in the design.

Requirements
Must have
• we are looking for a space to write the name or address of our customer, include 2 specials ( 1 for pest control, 1 for Lawn fertilization and weed control) that make the neighbors feel like they are getting a deal because they are neighbors of our customer.
• the back side of the postcard will list our range of services and have a space for the salesman to write his name.
• This will be printed on a glossy cardstock (unless the designer suggests something else).
• Phone numbers, Website, logos

```html
<!DOCTYPE html>
<html lang="en">
<head>
<meta charset="utf-8">
<title>Fieldmore Neighbor Door Hanger</title>
<link rel="stylesheet" href="https://fonts.googleapis.com/css2?family=Montserrat:wght@600;700;800&family=Nunito+Sans:wght@300;400&family=Libre+Baskerville:ital,wght@0,700;1,400&display=swap">
<style>
  :root {
    --page: #e9e9e7;
    --card: #ffffff;
    --leaf: #2f8f3e;
    --moss: #556b2f;
    --olive: #7a6a3a;
    --tan: #b39a68;
    --ink: #111111;
    --slate: #2e4a4f;
    --teal-grey: #6f9aa0;
    --body-grey: #444444;
    --badge: #f3c11f;
  }
  * { box-sizing: border-box; margin: 0; padding: 0; }
  html, body { width: 960px; height: 1200px; overflow: hidden; }
  body { background: var(--page); position: relative; font-family: "Nunito Sans", sans-serif; }

  .hanger {
    position: absolute; top: 52px; width: 424px; height: 1076px;
    background: var(--card); overflow: hidden;
    box-shadow: 0 2px 8px rgba(0,0,0,0.15);
  }
  .hanger--front { left: 44px; }
  .hanger--back { left: 492px; }

  .hanger__hole {
    position: absolute; left: 154px; top: 42px; width: 116px; height: 116px;
    border-radius: 50%; background: var(--page); z-index: 5;
  }

  /* front */
  .front__art {
    position: absolute; left: 0; top: 0; width: 100%; height: 590px;
    background: linear-gradient(180deg, var(--moss) 0%, #5d6e35 32%, #a8955f 52%, #9b8553 75%, var(--olive) 100%);
  }
  .front__houses { position: absolute; left: 188px; top: 432px; z-index: 2; }
  .friends-frame {
    position: absolute; left: 28px; top: 464px; width: 368px; height: 80px;
    border: 2px solid #fff; border-right: none; z-index: 2;
  }
  .friends-frame::after {
    content: ""; position: absolute; right: -2px; top: -2px; width: 2px; height: 72px; background: #fff;
  }
  .friends-frame__line1 {
    position: absolute; left: 16px; top: 6px; color: #fff;
    font: 700 29px/1 "Montserrat", sans-serif; letter-spacing: 8px;
  }
  .friends-frame__your {
    position: absolute; left: 16px; top: 48px; color: #fff;
    font: 600 24px/1 "Montserrat", sans-serif; letter-spacing: 6px;
  }
  .friends-frame__friends {
    position: absolute; left: 142px; top: 38px; color: #fff; background: var(--olive);
    padding-right: 4px; font: 800 38px/1 "Montserrat", sans-serif;
  }
  .front__lower {
    position: absolute; left: 0; top: 590px; width: 100%; height: 486px;
    background: linear-gradient(180deg, #f1f1f0 0%, #e6e6e4 55%, #ededeb 80%, #f7f7f6 100%);
  }
  .write-in {
    position: absolute; left: 50px; top: 566px; width: 324px; height: 62px;
    background: #fff; border-radius: 31px; z-index: 3;
    box-shadow: 0 1px 3px rgba(0,0,0,0.25);
  }
  .front__pitch {
    position: absolute; left: 0; top: 640px; width: 100%; text-align: center;
    font: italic 400 17px/23px "Libre Baskerville", serif; color: #333;
  }
  .coupon-rule {
    position: absolute; left: 0; width: 100%; height: 0;
    border-top: 3px dashed #111;
  }
  .coupon { position: absolute; left: 38px; }
  .coupon__kicker { font: 400 16px/1 "Nunito Sans", sans-serif; color: var(--ink); }
  .coupon__title { font: 800 25px/1 "Montserrat", sans-serif; color: var(--ink); margin-top: 2px; }
  .coupon__title--stack { font-size: 19px; line-height: 20px; }
  .coupon__note { font: italic 400 10px/1 "Libre Baskerville", serif; color: #222; margin-top: 7px; }
  .badge { position: absolute; left: 264px; width: 136px; height: 136px; z-index: 4; }

  .brand { position: absolute; left: 0; width: 100%; text-align: center; }
  .brand__name {
    display: inline-flex; align-items: center; gap: 10px;
    font: 700 26px/1 "Montserrat", sans-serif; color: var(--leaf);
  }
  .brand__mark { width: 18px; height: 18px; background: var(--leaf); }
  .brand__phone { display: block; margin-top: 12px; font: 800 24px/1 "Montserrat", sans-serif; color: var(--leaf); }
  .brand__web { display: block; margin-top: 4px; font: italic 400 16px/1 "Libre Baskerville", serif; color: var(--leaf); }

  /* back */
  .back__bg {
    position: absolute; inset: 0;
    background: linear-gradient(180deg, #f6f6f6 0%, #ededed 35%, #e8e8e8 55%, #f1f1f1 80%, #fbfbfb 100%);
  }
  .back__content { position: absolute; left: 0; top: 0; width: 100%; text-align: center; }
  .years__over, .years__label {
    position: absolute; left: 0; width: 100%;
    font: 600 28px/1 "Montserrat", sans-serif; letter-spacing: 8px; color: var(--teal-grey);
  }
  .years__over { top: 176px; }
  .years__num { position: absolute; left: 0; width: 100%; top: 206px; font: 600 86px/1 "Montserrat", sans-serif; color: var(--slate); }
  .years__label { top: 293px; }
  .back__family {
    position: absolute; left: 0; width: 100%; top: 330px;
    font: italic 400 19px/24px "Libre Baskerville", serif; color: #333;
  }
  .services__title {
    position: absolute; left: 0; width: 100%; top: 402px;
    font: 700 23px/1 "Montserrat", sans-serif; color: #2c2c2c;
  }
  .services__list {
    position: absolute; left: 0; width: 100%; top: 432px; list-style: none;
    font: 300 16px/19.4px "Nunito Sans", sans-serif; color: var(--body-grey);
  }
  .salesman__line {
    position: absolute; left: 64px; width: 296px; top: 840px;
    border-top: 3px dotted #333;
  }
  .salesman__label {
    position: absolute; left: 0; width: 100%; top: 852px;
    font: italic 400 19px/1 "Libre Baskerville", serif; color: #333;
  }
</style>
</head>
<body>

<section class="hanger hanger--front">
  <div class="front__art" role="img" aria-label="Paper cut-out illustration of two neighbors holding hands in front of houses on a green backdrop, with hand-lettered greeting Hey Neighbor"></div>
  <div class="hanger__hole"></div>

  <svg class="front__houses" width="48" height="34" viewBox="0 0 48 34" aria-hidden="true">
    <path d="M2 14 L14 2 L26 14 V34 H2 Z" fill="#fff"/>
    <path d="M24 20 L35 10 L46 20 V34 H24 Z" fill="#fff"/>
    <rect x="7" y="18" width="5" height="5" fill="#8f7b4c"/><rect x="15" y="18" width="5" height="5" fill="#8f7b4c"/>
    <rect x="7" y="26" width="5" height="5" fill="#8f7b4c"/><rect x="15" y="26" width="5" height="8" fill="#8f7b4c"/>
    <rect x="29" y="24" width="5" height="5" fill="#8f7b4c"/><rect x="37" y="24" width="5" height="10" fill="#8f7b4c"/>
  </svg>

  <div class="friends-frame">
    <span class="friends-frame__line1">WE SERVICE</span>
    <span class="friends-frame__your">YOUR</span>
    <span class="friends-frame__friends">FRIENDS</span>
  </div>

  <div class="front__lower" role="img" aria-label="Faded photo of a suburban home and front lawn"></div>
  <div class="write-in"></div>

  <p class="front__pitch">Because your friends use our services,<br>You get Neighborhood discounts!</p>

  <div class="coupon-rule" style="top:714px"></div>
  <div class="coupon" style="top:732px">
    <p class="coupon__kicker">Full Service</p>
    <p class="coupon__title">PEST CONTROL</p>
    <p class="coupon__note">You won't see a bug or we retreat for FREE</p>
  </div>
  <svg class="badge" style="top:694px" viewBox="0 0 136 136" aria-label="Only $9.95 first service">
    <circle cx="68" cy="68" r="64" fill="var(--badge)"/>
    <circle cx="68" cy="68" r="55" fill="none" stroke="#111" stroke-width="1.2"/>
    <g transform="rotate(-22 68 68)" fill="#111" text-anchor="middle">
      <text x="64" y="44" font-family="Montserrat, sans-serif" font-weight="700" font-size="13">ONLY</text>
      <text x="68" y="80" font-family="Libre Baskerville, serif" font-weight="700" font-size="34">$9.95</text>
      <text x="72" y="100" font-family="Libre Baskerville, serif" font-style="italic" font-size="12">First Service</text>
    </g>
  </svg>

  <div class="coupon-rule" style="top:812px"></div>
  <div class="coupon" style="top:826px">
    <p class="coupon__title coupon__title--stack">LAWN FERTILIZATION<br>&amp; WEED CONTROL</p>
    <p class="coupon__note">Thick Green Grass and No Weeds</p>
  </div>
  <svg class="badge" style="top:800px" viewBox="0 0 136 136" aria-label="Only $9.95 first service">
    <circle cx="68" cy="68" r="64" fill="var(--badge)"/>
    <circle cx="68" cy="68" r="55" fill="none" stroke="#111" stroke-width="1.2"/>
    <g transform="rotate(-22 68 68)" fill="#111" text-anchor="middle">
      <text x="64" y="44" font-family="Montserrat, sans-serif" font-weight="700" font-size="13">ONLY</text>
      <text x="68" y="80" font-family="Libre Baskerville, serif" font-weight="700" font-size="34">$9.95</text>
      <text x="72" y="100" font-family="Libre Baskerville, serif" font-style="italic" font-size="12">First Service</text>
    </g>
  </svg>
  <div class="coupon-rule" style="top:908px"></div>

  <div class="brand" style="top:946px">
    <span class="brand__name">Fieldmore <span class="brand__mark"></span></span>
    <span class="brand__phone">801-555-0147</span>
    <span class="brand__web">www.getfieldmore.com</span>
  </div>
</section>

<section class="hanger hanger--back">
  <div class="back__bg" role="img" aria-label="Faded photo of a two-story house"></div>
  <div class="hanger__hole"></div>

  <div class="back__content">
    <p class="years__over">OVER</p>
    <p class="years__num">25</p>
    <p class="years__label">YEARS</p>
    <p class="back__family">Family Owned Business<br>Operated in Salt Lake Side</p>

    <h2 class="services__title">Our List of Services</h2>
    <ul class="services__list">
      <li>Full Service Pest Control</li>
      <li>Inside &amp; Out Treatments</li>
      <li>Wasps/Hornets</li>
      <li>Mice/Rats</li>
      <li>Gophers/Voles</li>
      <li>Lawn Fertilization &amp; Weed Control</li>
      <li>Sprinkler Repairs &amp; Installation</li>
      <li>Wiring</li>
      <li>Xeriscape/Drip Conversion</li>
      <li>Landscape Design &amp; Install</li>
      <li>Pavers</li>
      <li>Pergolas/Pavilions</li>
      <li>Retaining walls</li>
      <li>Steel retaining</li>
      <li>Water features</li>
      <li>Landscape Lighting</li>
      <li>Fire features</li>
    </ul>

    <div class="salesman__line"></div>
    <p class="salesman__label">Authorised Salesman</p>
  </div>

  <div class="brand" style="top:948px">
    <span class="brand__name">Fieldmore <span class="brand__mark"></span></span>
    <span class="brand__phone">801-555-0147</span>
    <span class="brand__web">www.getfieldmore.com</span>
  </div>
</section>

</body>
</html>
```